Stonewell Holdings

Professional looking business card using darker colours
I do not yet have a logo for the company so feel free to suggest
The business is based on consultancy and project management
Based in Melbourne
Business card can omit the word "Holdings" and can be Stonewell consulting etc.

Contact Name on card : Ravi Pelunkoda Contact number : +61433 512 604 Email address will be confirmed shortly.

```html
<!DOCTYPE html>
<html lang="en">
<head>
<meta charset="utf-8">
<title>Stonewell Consulting Business Card</title>
<link href="https://fonts.googleapis.com/css2?family=Open+Sans:wght@300;400;700&display=swap" rel="stylesheet">
<style>
  :root {
    --ink: #211c1a;
    --blue: #007bc1;
    --teal: #00a0b6;
    --lavender: #bab3d6;
    --sky: #d6ebf9;
    --mist: #ececec;
    --paper: #f7f7f7;
    --white: #ffffff;
  }
  html, body {
    margin: 0;
    padding: 0;
    width: 918px;
    height: 1200px;
    overflow: hidden;
    background: var(--white);
  }
  .card-sheet {
    display: block;
    width: 918px;
    height: 1200px;
  }
  .brand-light { font-family: "Open Sans", sans-serif; font-weight: 300; fill: var(--white); }
  .brand-bold { font-family: "Open Sans", sans-serif; font-weight: 700; fill: var(--white); }
  .person-first { font-family: "Open Sans", sans-serif; font-weight: 300; fill: var(--white); }
  .person-last { font-family: "Open Sans", sans-serif; font-weight: 700; fill: var(--white); }
  .person-role { font-family: "Open Sans", sans-serif; font-weight: 300; fill: var(--white); }
  .contact-dark { font-family: "Open Sans", sans-serif; font-weight: 400; fill: var(--ink); }
  .contact-light { font-family: "Open Sans", sans-serif; font-weight: 400; fill: var(--white); }
</style>
</head>
<body>
<svg class="card-sheet" viewBox="0 0 1079 1411" preserveAspectRatio="none" xmlns="http://www.w3.org/2000/svg">
  <defs>
    <linearGradient id="front-haze" x1="0" y1="0" x2="0" y2="1">
      <stop offset="0" stop-color="#e9e9e9"/>
      <stop offset="1" stop-color="#ffffff"/>
    </linearGradient>
  </defs>

  <!-- Front face -->
  <g class="card-front">
    <rect class="front-base" x="0" y="0" width="1079" height="654" fill="url(#front-haze)"/>
    <polygon class="stripe-sky" points="0,0 40,0 388,654 268,654 0,158" fill="var(--sky)"/>
    <polygon class="stripe-blue" points="40,0 335,0 680,654 388,654" fill="var(--blue)"/>
    <polygon class="stripe-teal" points="335,0 460,0 808,654 680,654" fill="var(--teal)"/>
    <polygon class="stripe-lavender" points="460,0 520,0 868,654 808,654" fill="var(--lavender)"/>
    <polygon class="field-dark" points="520,0 1079,0 1079,654 868,654" fill="var(--ink)"/>
    <rect class="front-frame" x="23.5" y="27.5" width="1032" height="598" fill="none" stroke="var(--white)" stroke-width="1"/>
    <text class="brand-name" x="539" y="348" font-size="56" text-anchor="middle">
      <tspan class="brand-light">STONEWELL </tspan><tspan class="brand-bold">CONSULTING</tspan>
    </text>
  </g>

  <!-- Back face -->
  <g class="card-back">
    <rect class="back-base" x="0" y="757" width="1079" height="654" fill="var(--paper)"/>
    <rect class="back-frame" x="23.5" y="785.5" width="1032" height="598" fill="none" stroke="var(--white)" stroke-width="1.5"/>

    <polygon class="name-accent" points="446,830 513,830 595,977 527,977" fill="var(--blue)"/>
    <polygon class="name-band" points="513,830 1079,830 1079,977 595,977" fill="var(--ink)"/>
    <text class="person-name" x="985" y="905" font-size="42" text-anchor="end">
      <tspan class="person-first">RAVI </tspan><tspan class="person-last">PELUNKODA</tspan>
    </text>
    <text class="person-role" x="985" y="945" font-size="34" text-anchor="end">Your Definition</text>

    <rect class="web-band" x="0" y="1159" width="1079" height="86" fill="var(--sky)"/>
    <polygon class="address-band" points="0,1245 656,1245 738,1411 0,1411" fill="var(--ink)"/>
    <polygon class="address-mist" points="656,1245 722,1245 805,1411 738,1411" fill="var(--mist)"/>
    <polygon class="address-blue" points="722,1245 1079,1245 1079,1411 805,1411" fill="var(--blue)"/>
    <rect class="back-frame-lower" x="23.5" y="1245" width="1032" height="138.5" fill="none" stroke="var(--white)" stroke-width="1"/>

    <!-- Phone icon -->
    <path class="icon-phone" fill="var(--ink)"
      d="M111,1094 c3,-2 6,-1 7,1 l5,8 c1,2 0,4 -2,5 l-3,2 c2,5 6,9 11,11 l2,-3 c1,-2 3,-3 5,-2 l8,5 c2,1 3,4 1,7 l-3,3 c-3,3 -8,3 -13,1 c-10,-5 -18,-13 -22,-23 c-2,-5 -1,-10 1,-13 z"/>
    <text class="contact-dark" x="166" y="1100" font-size="26">+61433 512 604</text>
    <text class="contact-dark" x="166" y="1136" font-size="26">+61433 512 715</text>

    <!-- Globe icon -->
    <g class="icon-globe">
      <circle cx="121" cy="1200" r="17" fill="var(--ink)"/>
      <path d="M110,1192 c4,-3 9,-1 10,3 c1,4 -3,5 -2,9 c1,3 -3,6 -6,4 c-3,-3 -6,-12 -2,-16 z M125,1188 c4,0 9,4 10,9 c-3,1 -6,-1 -8,-3 c-2,-2 -4,-4 -2,-6 z M126,1202 c3,-2 7,0 7,3 c-1,4 -4,7 -8,8 c-2,-3 -1,-8 1,-11 z"
        fill="var(--sky)"/>
    </g>
    <text class="contact-dark" x="166" y="1189" font-size="26">ravi@stonewellconsulting.com</text>
    <text class="contact-dark" x="166" y="1225" font-size="26">www.stonewellconsulting.com</text>

    <!-- Pin icon -->
    <path class="icon-pin" fill="var(--white)" fill-rule="evenodd"
      d="M121,1288 c-8,0 -14,6 -14,14 c0,10 14,24 14,24 c0,0 14,-14 14,-24 c0,-8 -6,-14 -14,-14 z M121,1296 a6,6 0 1,0 0.01,0 z"/>
    <text class="contact-light" x="168" y="1296" font-size="26">Your City Melbourne</text>
    <text class="contact-light" x="168" y="1332" font-size="26">Street Location, Australia</text>
  </g>
</svg>
</body>
</html>
```